Menu Edit

Hello. We need a pricing edit on our current menu and new logo swapped (we already have the new logo), as well as colour changes. Also, we require a takeaway menu, in-store menu and footpath a-frame edit as well. I have attached the files bellow.

```html
<!DOCTYPE html>
<html lang="en">
<head>
<meta charset="utf-8">
<title>Tideline Fish &amp; Chips – Menu Set</title>
<link rel="stylesheet" href="https://fonts.googleapis.com/css2?family=Zilla+Slab:wght@300;400;600;700&family=Poppins:wght@400;500;600;700;800&display=swap">
<style>
  :root{
    --paper:#ffffff;
    --board:#231f20;
    --ink:#ffffff;
    --blue:#1a9bf0;
    --rule:#8a8788;
    --green:#1fb84c;
    --yellow:#f3d21b;
    --teal:#19c3c4;
    --orange:#f07c1a;
    --red:#e8331f;
  }
  *{margin:0;padding:0;box-sizing:border-box}
  html,body{width:1200px;height:2400px;overflow:hidden;background:var(--paper)}
  body{position:relative;font-family:'Poppins',sans-serif;color:var(--ink)}
  .panel{position:absolute;background:var(--board);overflow:hidden}
  .t{position:absolute;white-space:nowrap;line-height:1}
  .center{left:0;right:0;text-align:center}
  .slab{font-family:'Zilla Slab',serif}
  .blue{color:var(--blue)}

  /* brand lockup */
  .brand{position:absolute;display:flex;align-items:center;gap:14px}
  .brand-mark{border:3px solid var(--ink);border-radius:50%;flex:none}
  .brand-name{font-family:'Zilla Slab',serif;font-weight:300;color:var(--ink);line-height:1.05;letter-spacing:.02em}
  .brand-name span{display:block;font-size:.62em;letter-spacing:.06em;text-align:center}

  .btn{position:absolute;background:var(--blue);color:#fff;font-weight:700;border-radius:5px;display:flex;align-items:center;justify-content:center;white-space:nowrap}
  .badge{position:absolute;border-radius:2px}
  .rule{position:absolute;height:3px;background:var(--blue)}

  /* intro copy */
  .intro-copy{position:absolute;left:0;right:0;text-align:center;font-size:10.2px;line-height:13px;white-space:nowrap}
  .intro-note{position:absolute;left:0;right:0;text-align:center;font-size:10.8px;line-height:1;white-space:nowrap}

  /* menu pages */
  .sect-head{position:absolute;font-family:'Zilla Slab',serif;font-weight:600;font-size:20px;line-height:1;white-space:nowrap}
  .sect-head::after{content:"";position:absolute;left:0;bottom:-6px;width:16px;height:2px;background:var(--blue)}
  .menu-list{position:absolute;list-style:none}
  .menu-list li{display:flex;align-items:center;border-bottom:1px solid var(--rule);font-size:8.5px;white-space:nowrap}
  .menu-list b{font-weight:500}
  .item-name{color:var(--blue);font-weight:500}
  .framed{position:absolute;border:1px solid #bdbbbb;outline:1px solid #bdbbbb;outline-offset:-4px}
  .dish{position:absolute;left:10px;right:12px;font-size:7.5px;line-height:1.25}
  .dish h4{font-size:8.5px;font-weight:600;margin-bottom:2px}
  .dish p{color:#e6e6e6}
  .deco{position:absolute;border:3px solid var(--blue);border-radius:50%}
</style>
</head>
<body>

<!-- Board: welcome sign -->
<section class="panel welcome-board" style="left:144px;top:97px;width:437px;height:648px">
  <div class="brand" style="left:70px;top:60px">
    <div class="brand-mark" style="width:22px;height:22px"></div>
    <div class="brand-name" style="font-size:26px">TIDELINE<span>FISH &amp; CHIPS</span></div>
  </div>
  <div class="t center blue" style="top:175px;font-size:12px;letter-spacing:.55em;font-weight:500">WELCOME</div>
  <div class="t center slab" style="top:217px;font-size:38px;font-weight:700">Open Every Day</div>
  <div class="t center slab" style="top:269px;font-size:22px;font-weight:300"><span class="blue">Tues – Sun</span>&nbsp; Lunch 12pm – 3pm</div>
  <div class="t center slab" style="top:293px;font-size:22px;font-weight:300"><span class="blue">Tues – Sun</span>&nbsp; Dinner 5pm – 9pm</div>
  <div class="t center slab" style="top:332px;font-size:19px;font-weight:300">DINE IN <span class="blue">|</span> TAKEAWAY</div>
  <div class="t center slab" style="top:355px;font-size:19px;font-weight:300">ONLINE ORDERING &amp; DELIVER</div>
  <div class="t center slab" style="top:377px;font-size:19px;font-weight:300">FRESH RETAIL</div>
  <div class="t center" style="top:408px;font-size:12.5px;font-weight:700">BYO Welcome! Wine, Beer &amp; Spirits / Soft Drinks Available</div>
  <div class="rule" style="left:35px;width:367px;top:433px"></div>
  <div class="t center" style="top:441px;font-size:16px;font-weight:500">Choose your preparation:</div>
  <div class="t center" style="top:463px;font-size:14px;font-weight:500">PANKO CRUMBED / TEMPURA BATTERED / GRILLED</div>
  <div class="rule" style="left:35px;width:367px;top:486px"></div>
  <div class="t center" style="top:518px;font-size:45px;font-weight:800;letter-spacing:.02em">
    <svg width="40" height="34" viewBox="0 0 40 34" style="vertical-align:-2px;margin-right:4px" aria-hidden="true"><path d="M3 12c0-7 34-7 34 0v3h-9v-4c-5-2-11-2-16 0v4H3z" fill="#fff"/><path d="M9 17h22l5 15H4z" fill="#fff"/><circle cx="20" cy="24" r="4" fill="#231f20"/></svg>3555 0142
  </div>
  <div class="btn" style="left:62px;top:580px;width:314px;height:30px;font-size:19px;border-radius:8px">www.tidelinefishery.com.au</div>
</section>

<!-- Board: open sign -->
<section class="panel open-board" style="left:619px;top:97px;width:437px;height:648px">
  <div class="brand" style="left:95px;top:45px">
    <div class="brand-mark" style="width:20px;height:20px"></div>
    <div class="brand-name" style="font-size:26px">TIDELINE<span>FISH &amp; CHIPS</span></div>
  </div>
  <div class="t center slab" style="top:142px;font-size:86px;font-weight:300;letter-spacing:.02em">WE’RE</div>
  <div class="t center slab" style="top:212px;font-size:86px;font-weight:300;letter-spacing:.02em">OPEN!</div>
  <div class="btn" style="left:124px;top:357px;width:192px;height:32px;font-size:16px">ORDER FOR PICKUP</div>
  <div class="t center" style="top:403px;font-size:13.5px"><span class="blue">●</span> www.tidelinefishery.com.au</div>
  <div class="t center" style="top:422px;font-size:27px;font-weight:700">☎ 3555 0142</div>
  <div class="btn" style="left:124px;top:482px;width:192px;height:31px;font-size:16px">ORDER FOR DELIVERY</div>
  <div class="badge" style="left:124px;top:531px;width:32px;height:32px;background:var(--green)"></div>
  <div class="badge" style="left:160px;top:531px;width:72px;height:32px;background:var(--yellow)"></div>
  <div class="badge" style="left:236px;top:531px;width:80px;height:32px;background:var(--teal)"></div>
  <div class="badge" style="left:122px;top:575px;width:84px;height:17px;background:var(--orange)"></div>
  <div class="badge" style="left:218px;top:578px;width:99px;height:11px;background:var(--red)"></div>
</section>

<!-- Menu cover -->
<section class="panel menu-cover" style="left:267px;top:778px;width:649px;height:490px">
  <div class="brand" style="left:150px;top:50px;gap:24px">
    <div class="brand-mark" style="width:28px;height:28px"></div>
    <div class="brand-name" style="font-size:36px">TIDELINE<span>FISH &amp; CHIPS</span></div>
  </div>
  <p class="intro-copy" style="top:159px">Our premium quality fish is wild caught and sustainably farmed from pristine Australian &amp;<br>New Zealand waters, delivered in-store every day for you to enjoy! &nbsp;Our seafood is deep-fried<br>to golden goodness with premium 100% Australian grown and pressed sunflower oil.</p>
  <p class="intro-note" style="top:202px">(All seafood is subject to daily fresh market availability).</p>
  <div class="t" style="left:113px;width:200px;text-align:center;top:252px;font-size:10px;font-weight:600">Gluten friendly options are available.</div>
  <div class="t" style="left:113px;width:200px;text-align:center;top:270px;font-size:10px;font-weight:600">Our takeaway packaging is ◯ friendly.</div>
  <div class="t" style="left:343px;width:200px;text-align:center;top:252px;font-size:10px;font-weight:600">Menu substitutions are not available.</div>
  <div class="t" style="left:343px;width:200px;text-align:center;top:270px;font-size:10px;font-weight:600">Public Holiday surcharge 15%.</div>
  <div class="btn" style="left:154px;top:325px;width:142px;height:23px;font-size:11.5px;border-radius:3px">ORDER FOR PICKUP</div>
  <div class="btn" style="left:333px;top:325px;width:144px;height:23px;font-size:11.5px;border-radius:3px">ORDER FOR DELIVERY</div>
  <div class="t" style="left:154px;width:142px;text-align:center;top:364px;font-size:9.5px"><span class="blue">●</span> www.tidelinefishery.com.au</div>
  <div class="t" style="left:154px;width:142px;text-align:center;top:380px;font-size:14px;font-weight:700">☎ 3555 0142</div>
  <div class="badge" style="left:333px;top:357px;width:24px;height:23px;background:var(--green)"></div>
  <div class="badge" style="left:361px;top:357px;width:51px;height:23px;background:var(--yellow)"></div>
  <div class="badge" style="left:416px;top:357px;width:61px;height:23px;background:var(--teal)"></div>
  <div class="badge" style="left:333px;top:388px;width:62px;height:13px;background:var(--orange)"></div>
  <div class="badge" style="left:404px;top:391px;width:73px;height:8px;background:var(--red)"></div>
  <div class="t center" style="top:425px;font-size:18px">Follow us &nbsp;<span style="display:inline-block;width:16px;height:16px;background:var(--orange);border-radius:3px;vertical-align:-2px"></span> tidelinefish_riverside</div>
</section>

<!-- Menu inside: starters, burgers, kids -->
<section class="panel menu-page-one" style="left:267px;top:1297px;width:649px;height:491px">
  <h2 class="sect-head" style="left:43px;top:35px">Starters &amp; Sides</h2>
  <ul class="menu-list" style="left:43px;top:64px;width:260px">
    <li style="height:16.2px">Crumbed Calamari (8)</li>
    <li style="height:16.2px">Salt &amp; Pepper Calamari (8)</li>
    <li style="height:16.2px">Crumbed Sea Scallop</li>
    <li style="height:16.2px">Crumbed Prawn</li>
    <li style="height:16.2px">BBQ Prawn Skewer</li>
    <li style="height:16.2px">Onion Rings (8)</li>
    <li style="height:16.2px">Popcorn Chicken</li>
    <li style="height:16.2px">Potato Scallop</li>
    <li style="height:16.2px">Grilled Halloumi (3 slices)</li>
    <li style="height:16.2px">Fried Halloumi (3 slices, crumbed)</li>
  </ul>
  <h2 class="sect-head" style="left:43px;top:246px">Chips</h2>
  <ul class="menu-list" style="left:43px;top:277px;width:260px">
    <li style="height:16.2px">Chips GF</li>
    <li style="height:16.2px">Beer Battered Chips</li>
    <li style="height:16.2px">Sweet Potato Chips</li>
  </ul>
  <h2 class="sect-head" style="left:43px;top:366px">Sauces</h2>
  <ul class="menu-list" style="left:43px;top:396px;width:266px">
    <li style="height:16px">Tartare, Aioli, Tomato &amp; Chipotle Mayonnaise</li>
  </ul>

  <div class="framed" style="left:335px;top:38px;width:270px;height:239px">
    <h2 class="sect-head" style="left:10px;top:13px">Burgers &amp; Tacos</h2>
    <div class="dish" style="top:48px"><h4><span class="item-name">Fish Burger</span> &amp; chips</h4><p>Crumbed cod fillet, shredded lettuce, tomato &amp; tartare sauce in a toasted bun.</p></div>
    <div class="dish" style="top:94px"><h4><span class="item-name">Fish Tacos</span> (3) &amp; chips</h4><p>Beer battered cod, shredded red &amp; green cabbage, carrot, chipotle mayonnaise in soft flour tortillas.</p></div>
    <div class="dish" style="top:144px"><h4><span class="item-name">Chicken Burger</span> &amp; chips</h4><p>Grilled free range chicken tenders, shredded lettuce, tomato, cheese, avocado, aioli in a toasted bun.</p></div>
    <div class="dish" style="top:194px"><h4><span class="item-name">Steak Burger</span> &amp; chips</h4><p>Grilled grass fed rib fillet, shredded lettuce, tomato, cheese, caramelised onion, BBQ sauce in a toasted bun.</p></div>
    <div style="position:absolute;left:10px;right:12px;top:88px;border-top:1px solid var(--rule)"></div>
    <div style="position:absolute;left:10px;right:12px;top:138px;border-top:1px solid var(--rule)"></div>
    <div style="position:absolute;left:10px;right:12px;top:188px;border-top:1px solid var(--rule)"></div>
  </div>

  <h2 class="sect-head" style="left:335px;top:332px">Children’s Fish &amp; Chips</h2>
  <ul class="menu-list" style="left:335px;top:361px;width:264px">
    <li style="height:16px"><span class="item-name">Fish Fingers</span>&nbsp;(4) &amp; chips</li>
    <li style="height:16px"><span class="item-name">Crumbed Calamari</span>&nbsp;(4) &amp; chips</li>
    <li style="height:16px"><span class="item-name">Popcorn Chicken</span>&nbsp;&amp; chips</li>
  </ul>
  <div class="deco" style="left:24px;top:454px;width:14px;height:14px;border-color:#fff"></div>
</section>

<!-- Menu inside: fish, salads, platters -->
<section class="panel menu-page-two" style="left:267px;top:1823px;width:649px;height:491px">
  <div class="framed" style="left:43px;top:23px;width:269px;height:236px">
    <h2 class="sect-head" style="left:10px;top:11px">Fish &amp; Chips</h2>
    <div class="t" style="left:10px;top:41px;font-size:7.8px">Served with your choice of chips, tartare sauce &amp; lemon.</div>
    <ul class="menu-list" style="left:10px;top:55px;width:247px">
      <li style="height:14.6px;font-size:8px"><span class="item-name">Cod</span>&nbsp;<b>&amp; chips</b>&nbsp;(NZ, wild caught)</li>
      <li style="height:14.6px;font-size:8px"><span class="item-name">Whiting</span>&nbsp;<b>&amp; chips</b>&nbsp;(QLD, wild caught, crumbed only)</li>
      <li style="height:14.6px;font-size:8px"><span class="item-name">Flathead</span>&nbsp;<b>&amp; chips</b>&nbsp;(SA, wild caught, beer battered only)</li>
      <li style="height:14.6px;font-size:8px"><span class="item-name">Snapper</span>&nbsp;<b>&amp; chips</b>&nbsp;(NT, wild caught)</li>
      <li style="height:14.6px;font-size:8px"><span class="item-name">Barramundi</span>&nbsp;<b>&amp; chips</b>&nbsp;(NT, ocean farmed)</li>
      <li style="height:14.6px;font-size:8px"><span class="item-name">Salmon</span>&nbsp;<b>&amp; chips</b>&nbsp;(TAS, ocean farmed)</li>
      <li style="height:14.6px;font-size:8px"><span class="item-name">Crumbed Calamari</span>&nbsp;(8) &amp; chips</li>
      <li style="height:14.6px;font-size:8px"><span class="item-name">Salt &amp; Pepper Calamari</span>&nbsp;(8) &amp; chips</li>
      <li style="height:14.6px;font-size:8px"><span class="item-name">Crumbed Prawns</span>&nbsp;(5) &amp; chips</li>
      <li style="height:14.6px;font-size:8px"><span class="item-name">BBQ Prawn Skewers</span>&nbsp;(2) &amp; chips</li>
    </ul>
    <div class="t center" style="top:211px;font-size:7.8px"><span class="item-name">Made fresh to order</span> | Choose your preparation:</div>
    <div class="t center" style="top:221px;font-size:7.5px;font-weight:600">GRILLED / CRUMBED / BEER BATTERED</div>
  </div>

  <h2 class="sect-head" style="left:335px;top:36px">Salads</h2>
  <div class="t" style="left:335px;top:67px;font-size:8px;font-weight:500">Freshly prepared to order using the freshest local produce.</div>
  <div class="dish" style="left:335px;right:44px;top:93px;font-size:7px"><h4 class="item-name" style="font-size:8px">Greek</h4><p>Lettuce, cucumber, tomato, red onion, Kalamata olives, feta, Greek peppers, wild oregano, dressed in Greek extra virgin olive oil vinaigrette.</p></div>
  <div class="dish" style="left:335px;right:44px;top:142px;font-size:7px"><h4 class="item-name" style="font-size:8px">Roast Pumpkin</h4><p>Roast pumpkin, wild rocket, Parmigiano Reggiano, toasted pine nuts, dressed in Greek extra virgin olive oil &amp; vintage balsamic vinegar.</p></div>
  <div class="dish" style="left:335px;right:44px;top:190px;font-size:7px"><h4 class="item-name" style="font-size:8px">Slaw</h4><p>Shredded red &amp; green cabbage, carrot, tossed in a light mayonnaise dressing.</p></div>
  <div class="dish" style="left:335px;right:44px;top:230px;font-size:7px"><h4 class="item-name" style="font-size:8px">Asian Slaw</h4><p>Shredded red &amp; green cabbage, carrot, spring onion, crispy noodles, sesame seeds, tossed in a sweet soy dressing.</p></div>
  <div style="position:absolute;left:335px;width:268px;top:133px;border-top:1px solid var(--rule)"></div>
  <div style="position:absolute;left:335px;width:268px;top:181px;border-top:1px solid var(--rule)"></div>
  <div style="position:absolute;left:335px;width:268px;top:221px;border-top:1px solid var(--rule)"></div>
  <div class="deco" style="left:604px;top:30px;width:16px;height:16px;border-color:#fff"></div>

  <h2 class="sect-head" style="left:43px;top:308px">Cooked Seafood Platters</h2>
  <div class="t" style="left:43px;top:341px;width:562px;font-size:7.5px;line-height:1.2;white-space:normal">Cooked Seafood Platters include: whiting, calamari, salt &amp; pepper calamari, prawns, sea scallops, chips, one of our freshly made salads, tartare sauce &amp; lemon.</div>
  <ul class="menu-list" style="left:43px;top:368px;width:563px">
    <li style="height:17px;font-weight:600;font-size:8px">Cooked Platter for One</li>
    <li style="height:17px;font-weight:600;font-size:8px">Cooked Platter for Two</li>
    <li style="height:17px;font-weight:600;font-size:8px;border-bottom:none">Cooked Platter for Three</li>
  </ul>
  <div class="t center" style="top:426px;font-size:7.5px">Our seafood platters are available crumbed only.</div>
</section>

</body>
</html>
```